Renaldo's Motorworks landing page to Dealership page, Rental Car Page, and Auto Body page.

I'm looking for my website to have RenaldosMotor.com be the landing page. From there visitors will have the option to visit three pages. My auto dealer page, of which I will provide an example of how I'd like it done. Auto body page, where I will fill in the text. The rental car page. Basically on the auto dealer and rental page I'll need the ability to add vehicles and delete as I need. Otherwise, its a pretty straightforward site. Nothing extensive. I already have the logo design from a previous project on here completed and can provide. If more funded needed for page capabilities, I can provide. I do have an account with HostPeak, with renaldosmotor.com already under them.

Target Market(s)

Automotive

Industry/Entity Type

Auto body repair, dealership, rental car.

Coding

Coded - Design and coding required

Number of Pages Required

4 page

Font styles to use
Sans Serif

Colors
0054AA
0677BA
7BADD7
CADEEF
E8F1F8

Requirements
Must have
• My logo Renaldos Motorworks at the top. Be creative with pics in the background of cars.
Nice to have
• Ease of use with being able to add vehicles for sale, and rental cars.
Should not have
• Nothing complex, would like to get in and out. Nothing to extensive on the designs of the pages, simple but attractive.

```html
<!DOCTYPE html>
<html lang="en">
<head>
<meta charset="utf-8">
<title>Renaldo's Motorworks – About Us</title>
<link href="https://fonts.googleapis.com/css2?family=Roboto:wght@400;500;700&display=swap" rel="stylesheet">
<style>
:root{
  --navy:#0054AA;
  --blue:#0677BA;
  --sky:#7BADD7;
  --pale:#CADEEF;
  --mist:#E8F1F8;
  --ink:#111;
  --text:#333;
  --footer:#0c0c0c;
}
*{box-sizing:border-box;margin:0;padding:0}
html,body{width:1200px;height:3731px;overflow:hidden;background:#fff}
body{position:relative;font-family:'Roboto',Arial,sans-serif;color:var(--text)}
.abs{position:absolute}
.topbar{left:0;top:0;width:1200px;height:45px;background:var(--navy);color:#fff;font-size:14px;font-weight:500;text-align:center;line-height:45px}
.brand{left:55px;top:78px;width:150px;color:var(--navy);font-size:30px;font-weight:700;line-height:1;letter-spacing:.5px}
.brand small{display:block;font-size:13px;font-weight:700;letter-spacing:2px;margin-top:6px}
.search{left:443px;top:68px;width:542px;height:36px;border:1px solid #ccc;font-size:13px;color:#555;padding:0 14px;line-height:34px}
.search .btn{position:absolute;right:-1px;top:-1px;width:38px;height:36px;background:var(--blue);display:flex;align-items:center;justify-content:center}
.social{top:70px;width:32px;height:32px;border-radius:50%}
.info{top:120px;font-size:14px;color:#444;display:flex;align-items:center;gap:6px;height:20px}
.info.big{font-size:18px;font-weight:500;color:var(--navy)}
.nav{left:0;top:166px;width:1200px;height:47px;background:var(--blue)}
.nav a{position:absolute;top:0;line-height:47px;color:#fff;font-size:15px;font-weight:500;text-decoration:none}
h1.title{left:0;width:1200px;text-align:center;font-size:44px;font-weight:700;color:var(--ink)}
.intro{left:135px;top:331px;width:930px;text-align:center;font-size:15px;line-height:27.5px;color:#333}
.col{top:490px;width:345px}
.col h2{font-size:24px;font-weight:500;color:var(--ink);margin-bottom:14px}
.col p{font-size:14.6px;line-height:27.5px}
.photo{left:0;top:800px;width:1200px;height:495px;background:radial-gradient(ellipse at 50% 60%,#1f4a50 0%,#243028 30%,#3a2e22 60%,#1a1612 100%)}
.subtitle{left:0;top:1458px;width:1200px;text-align:center;font-size:15px;font-weight:500;color:#222}
.line{left:599px;top:1565px;height:855px;border-left:2px dashed var(--blue)}
.dot{left:592px;width:17px;height:17px;border-radius:50%;background:var(--blue);box-shadow:0 0 0 4px var(--pale)}
.card{width:463px;background:#fff;box-shadow:0 2px 12px rgba(0,0,0,.12);padding:24px 20px 20px}
.card h3{font-size:22px;font-weight:500;color:var(--ink);margin-bottom:10px}
.card p{font-size:11.3px;line-height:22.4px;color:#555}
.card.active{background:var(--blue)}
.card.active h3,.card.active p{color:#fff}
.card.active::before{content:"";position:absolute;left:-14px;top:72px;border:14px solid transparent;border-left:0;border-right-color:var(--blue)}
.card.left::after{content:"";position:absolute;right:-12px;top:105px;border:12px solid transparent;border-right:0;border-left-color:#fff}
.hours{left:0;top:2518px;width:1200px;height:419px;background:linear-gradient(180deg,#f7f2f2,#fbf4f4 60%,#f6eeee)}
.hours h4,.contact h4{font-size:18px;font-weight:500;color:var(--ink)}
.hrow{display:flex;font-size:15px;color:#222;height:27.8px;align-items:center}
.hrow span:first-child{width:109px}
.form{left:549px;top:2618px;width:451px;height:247px;background:#fff;padding:34px 27px}
.field{position:absolute;border:1px solid #ddd;font-size:12px;color:#333;padding:0 10px;line-height:32px;height:34px}
.submit{position:absolute;left:310px;top:185px;width:112px;height:38px;background:var(--blue);color:#fff;font-size:14px;font-weight:500;text-align:center;line-height:38px}
.map{left:0;top:2937px;width:1200px;height:418px;background:linear-gradient(135deg,#e9ecef,#dfe6dc 35%,#eceae6 60%,#e4e8ee)}
.footer{left:0;top:3355px;width:1200px;height:376px;background:var(--footer);color:#fff}
.footer h5{font-size:18px;font-weight:500;margin-bottom:14px}
.footer .links a{display:block;color:#fff;font-size:13.5px;text-decoration:none;line-height:28.6px}
.fi{display:flex;gap:12px;font-size:13.5px;line-height:22px;margin-bottom:12px}
.news{left:805px;top:3484px;width:300px;height:50px;border-radius:25px;background:#fff;overflow:hidden}
.news span{position:absolute;left:22px;top:0;line-height:50px;font-size:14px;color:#555}
.news .go{position:absolute;right:0;top:0;width:50px;height:50px;background:var(--blue);display:flex;align-items:center;justify-content:center}
.ring{top:3555px;width:36px;height:36px;border:1px solid #fff;border-radius:50%}
.rule{left:92px;top:3683px;width:1016px;border-top:1px solid #333}
.copy{left:0;top:3693px;width:1200px;text-align:center;font-size:14px}
</style>
</head>
<body>

<div class="abs topbar">COVID-19 UPDATES :&nbsp; The standard Lorem Ipsum passage, used</div>

<div class="abs brand" aria-label="Renaldo's Motorworks">RENALDO'S<small>MOTORWORKS</small></div>

<div class="abs search">Search our inventory
  <div class="btn"><svg width="16" height="16" viewBox="0 0 16 16"><circle cx="7" cy="7" r="5" fill="none" stroke="#fff" stroke-width="1.6"/><line x1="10.6" y1="10.6" x2="14.5" y2="14.5" stroke="#fff" stroke-width="1.6"/></svg></div>
</div>
<div class="abs social" style="left:1006px;background:var(--navy)"></div>
<div class="abs social" style="left:1046px;background:#1da1f2"></div>
<div class="abs social" style="left:1085px;background:#c4302b"></div>
<div class="abs social" style="left:1124px;background:#8a6a55"></div>

<div class="abs info" style="left:440px"><svg width="12" height="16" viewBox="0 0 12 16"><path d="M6 0a6 6 0 0 0-6 6c0 4.5 6 10 6 10s6-5.5 6-10a6 6 0 0 0-6-6zm0 8.5A2.5 2.5 0 1 1 6 3.5a2.5 2.5 0 0 1 0 5z" fill="var(--navy)"/></svg>1234 Somestreet Anywhere USA&nbsp; 21212</div>
<div class="abs info big" style="left:742px"><svg width="15" height="15" viewBox="0 0 16 16"><path d="M3.5 1l3 3-1.8 2a9 9 0 0 0 5.3 5.3l2-1.8 3 3-2 2.5C7 14.5 1.5 9 1 3.5z" fill="var(--navy)"/></svg>888 888 8888</div>
<div class="abs info big" style="left:907px"><svg width="20" height="14" viewBox="0 0 20 14"><rect x="1" y="1" width="18" height="12" fill="none" stroke="var(--navy)" stroke-width="2"/><path d="M1 1l9 7 9-7" fill="none" stroke="var(--navy)" stroke-width="2"/></svg>info@renaldosmotor.com</div>

<nav class="abs nav">
  <a style="left:255px">HOME</a>
  <a style="left:354px">AUTO BODY REPAIR</a>
  <a style="left:552px">DEALERSHIP</a>
  <a style="left:700px">RENTAL CAR</a>
  <a style="left:847px">CONTACT US</a>
</nav>

<h1 class="abs title" style="top:270px">ABOUT US</h1>
<p class="abs intro">Lorem ipsum dolor sit amet, consectetur adipiscing elit, sd do eiusmod tempor incididunt ut labore et dolore magna aliqua. Quis ipsum ndisse ultrices gravida. Risus commodo viverra maecenas accumsan lacus velilisis. Lorem ipsum dolor sit amet, consectetur adipiscing elit, sed do eiumod tempor incididunt ut labore et dolore magna aliqua. Quis ipsum suspesse ultrices gravida. Risus commodo viverra maecenas accumsan lacus vsLorem ipsum dolor sit amet, consectetur adipiscing elit, sd d</p>

<div class="abs col" style="left:55px"><h2>WHO WE ARE</h2><p>Lorem ipsum dolor sit amet, consectetur adiscing elit, sd do eiusmod tempor incididunt ut e et dolore magna aliqua. Quis ipsum ndissvida. Risus commodo viverra maecenas accumsan lacus velilisisorem ipsum dolor sit amet,Lorem ipsum dolor sit a consectetur adiscing elit, sd do eiusmod tempor incididunt ut e et dolore magna aliqua.</p></div>
<div class="abs col" style="left:431px"><h2>WHAT WE DO</h2><p>Lorem ipsum dolor sit amet, consectetur adiscing elit, sd do eiusmod tempor incididunt ut e et dolore magna aliqua. Quis ipsum ndissvida. Risus commodo viverra maecenas accumsan lacus velilisisorem ipsum dolor sit amet,Lorem ipsum dolor sit a consectetur adiscing elit, sd do eiusmod tempor incididunt ut e et dolore magna aliqua.</p></div>
<div class="abs col" style="left:808px"><h2>WHY WE DO IT</h2><p>Lorem ipsum dolor sit amet, consectetur adiscing elit, sd do eiusmod tempor incididunt ut e et dolore magna aliqua. Quis ipsum ndissvida. Risus commodo viverra maecenas accumsan lacus velilisisorem ipsum dolor sit amet,Lorem ipsum dolor sit a consectetur adiscing elit, sd do eiusmod tempor incididunt ut e et dolore magna aliqua.</p></div>

<div class="abs photo" role="img" aria-label="Dark SUV parked on a dirt road through a pine forest"></div>

<h1 class="abs title" style="top:1405px;font-size:38px">JOURNEY OF OUR STORY</h1>
<div class="abs subtitle">THE STANDARD LOREM IUSED SINCE THE 1500S</div>

<div class="abs line"></div>
<div class="abs dot" style="top:1707px"></div>
<div class="abs dot" style="top:1885px"></div>
<div class="abs dot" style="top:2016px"></div>
<div class="abs dot" style="top:2139px"></div>
<div class="abs dot" style="top:2294px"></div>

<div class="abs card left" style="left:100px;top:1598px;height:238px"><h3>2008</h3><p>Lorem ipsum dolor sit amet, consectetur adipiscing elit, sed do eiusmod tempor incididunt ut labore et dolore magna aliqua. Quis ipsum suspendisse ultrices gravida. Risus commodo viverra maecenas accumsan lacus vel facilisis. Lorem ipsum dolor sit amet, consectetur adipiscing elit, sed do eiusmod tempor incididunt ut labore et dolore magna aliqua. Quis ipsum suspendisse ultrices gravida. Risus commodo viverra maecenas accumsan lacus vel facilisis. Lorem ipsum dolor sit amet, consectetur adipiscing elit, sed do eiusmod t</p></div>
<div class="abs card active" style="left:636px;top:1800px;height:183px;padding-top:20px"><h3>2012</h3><p>Lorem ipsum dolor sit amet, consectetur adipiscing elit, sed do eiusmod tempor incididunt ut labore et dolore magna aliqua. Quis ipsum suspendisse ultrices gravida. Risus commodo viverra maecenas accumLorem ipsum dolor sit amet, consectetur adipiscing elit, sed do eiusmod tempor incididunt ut labore et dolore magna aliqua. Quis ipsum suspendisse ultrices gravida.</p></div>
<div class="abs card left" style="left:100px;top:1948px;height:142px"><h3>2013</h3><p>Lorem ipsum dolor sit amet, consectetur adipiscing elit, sed do eiusmod tempor incididunt ut labore et dolore magna aliqua. Quis ipsum suspendisse ultrices gravida. Risus commodo viverra maecenas accumsan lacus vel facilisis. Lorem</p></div>
<div class="abs card" style="left:636px;top:2055px;height:188px"><h3>2019</h3><p>Lorem ipsum dolor sit amet, consectetur adipiscing elit, sed do eiusmod tempor incididunt ut labore et dolore magna aliqua. Quis ipsum suspendisse ultrices gravida. Risus commodo viverra maecenas accumsan lacus vel facilisis. Lorem ipsum dolor sit amet, consectetur adipiscing elit, sed do eiusmod tempor incididunt ut labore et dolore magna aliqua</p></div>
<div class="abs card left" style="left:100px;top:2207px;height:190px"><h3>2021</h3><p>Lorem ipsum dolor sit amet, consectetur adipiscing elit, sed do eiusmod tempor incididunt ut labore et dolore magna aliqua. Quis ipsum suspendisse ultrices gravida. Risus commodo viverra maecenas accumsan lacus vel facilisis. Lorem ipsum dolor sit amet, consectetur adipiscing elit, sed do eiusmod tempor incididunt ut labore et dolore magna aliqua</p></div>

<section class="abs hours" role="img" aria-label="Faded photo of a car body in soft red tones behind showroom hours">
  <div class="abs" style="left:199px;top:70px">
    <h4 style="margin-bottom:6px">SHOWROOM HOURS</h4>
    <div class="hrow"><span>Monday</span><span>09:00 AM&nbsp; 08:00 PM</span></div>
    <div class="hrow"><span>Tuesday</span><span>09:00 AM&nbsp; 08:00 PM</span></div>
    <div class="hrow"><span>Wednesday</span><span>09:00 AM&nbsp; 08:00 PM</span></div>
    <div class="hrow"><span>Thursday</span><span>09:00 AM&nbsp; 08:00 PM</span></div>
    <div class="hrow"><span>Friday</span><span>09:00 AM&nbsp; 08:00 PM</span></div>
    <div class="hrow"><span>Saturday</span><span>09:00 AM&nbsp; 08:00 PM</span></div>
    <div class="hrow"><span>Sunday</span><span>09:00 AM&nbsp; 08:00 PM</span></div>
  </div>
  <h4 class="abs contact" style="left:549px;top:70px">CONTACT US</h4>
</section>
<div class="abs form">
  <div class="field" style="left:18px;top:34px;width:199px">First Name</div>
  <div class="field" style="left:224px;top:34px;width:199px">Last Name</div>
  <div class="field" style="left:18px;top:78px;width:199px">Email</div>
  <div class="field" style="left:224px;top:78px;width:199px">Phone</div>
  <div class="field" style="left:18px;top:122px;width:405px;height:48px">Message</div>
  <div class="submit">SUBMIT</div>
</div>

<div class="abs map" role="img" aria-label="Street map of the dealership area with a location marker"></div>

<footer class="abs footer">
  <div class="abs" style="left:100px;top:105px;width:190px;text-align:center;font-size:34px;font-weight:700;line-height:1">RENALDO'S<div style="font-size:14px;letter-spacing:2px;margin-top:8px">MOTORWORKS</div></div>
  <div class="abs links" style="left:355px;top:58px"><h5>QUICK LINK</h5><a>Home</a><a>Auto body repair</a><a>Dealership</a><a>Rental car</a><a>About Us</a><a>Contact Us</a></div>
  <div class="abs" style="left:528px;top:58px;width:230px"><h5>CONTACT US</h5>
    <div class="fi"><svg width="14" height="18" viewBox="0 0 12 16"><path d="M6 0a6 6 0 0 0-6 6c0 4.5 6 10 6 10s6-5.5 6-10a6 6 0 0 0-6-6zm0 8.5A2.5 2.5 0 1 1 6 3.5a2.5 2.5 0 0 1 0 5z" fill="#fff"/></svg><span>1234 Somestreet Anywhere<br>USA 21212</span></div>
    <div class="fi"><svg width="16" height="14" viewBox="0 0 20 14"><rect x="1" y="1" width="18" height="12" fill="none" stroke="#fff" stroke-width="2"/><path d="M1 1l9 7 9-7" fill="none" stroke="#fff" stroke-width="2"/></svg><span>Email:<br>info@renaldosmotor.com</span></div>
    <div class="fi"><svg width="14" height="14" viewBox="0 0 16 16"><path d="M3.5 1l3 3-1.8 2a9 9 0 0 0 5.3 5.3l2-1.8 3 3-2 2.5C7 14.5 1.5 9 1 3.5z" fill="#fff"/></svg><span>Phone:<br>(123) 456 7890</span></div>
  </div>
  <div class="abs" style="left:812px;top:58px"><h5>OUR NEWSLETTER</h5><div style="font-size:13.5px">Sign up to stay in the Renaldo's Motorworks loop</div></div>
</footer>
<div class="abs news"><span>Enter Email</span><div class="go"><svg width="20" height="18" viewBox="0 0 20 18"><path d="M0 8L20 0 16 18 9 12 15 4 7 11z" fill="#fff"/></svg></div></div>
<div class="abs ring" style="left:820px"></div>
<div class="abs ring" style="left:863px"></div>
<div class="abs ring" style="left:907px"></div>
<div class="abs ring" style="left:951px"></div>
<div class="abs rule"></div>
<div class="abs copy" style="color:#fff">Copyright © 2021 Renaldo's Motorworks. All rights</div>

</body>
</html>
```